Oru Loft Business Card

We need a business card designed for a a company called "Oru Loft". We offer consulting, coaching and training to business leaders and coaches (across the world) using the latest findings in neuroscience, social and emotional intelligence and positive psychology. The final design should communicate the use of brain science to create sustainable relationships.

The card should be doublesided. The logo is attached and names and titles will be provided to the successful designer. Thank you.

```html
<!DOCTYPE html>
<html lang="en">
<head>
<meta charset="utf-8">
<title>Oru Loft Business Card</title>
<link rel="stylesheet" href="https://fonts.googleapis.com/css2?family=Arimo:wght@400;700&display=swap">
<style>
  :root {
    --stage: #ecebe8;
    --card-light: #ffffff;
    --card-dark: #1f1f20;
    --blue: #1a8fd0;
    --lime: #b2d235;
    --ink: #2b2b2b;
    --ghost: #efefef;
  }
  * { box-sizing: border-box; margin: 0; padding: 0; }
  html, body { width: 1200px; height: 646px; overflow: hidden; }
  body {
    background: var(--stage);
    font-family: "Arimo", Arial, sans-serif;
    position: relative;
  }
  .card {
    position: absolute;
    top: 173px;
    width: 520px;
    height: 300px;
    overflow: hidden;
    box-shadow: 0 6px 18px rgba(0,0,0,0.12);
  }
  .card--front { left: 50px; background: var(--card-light); }
  .card--back { left: 630px; background: var(--card-dark); }

  .accent { position: absolute; width: 18px; }
  .card--front .accent--lime { right: 0; top: 0; height: 64px; background: var(--lime); }
  .card--back .accent--lime { right: 0; top: 30px; height: 72px; background: var(--lime); }
  .card--back .accent--blue { left: 0; bottom: 30px; height: 80px; background: var(--blue); }

  .ghost-mark {
    position: absolute; right: 40px; top: -70px;
    width: 230px; height: 230px; border-radius: 50%;
    background: var(--ghost);
  }

  .brand { display: flex; align-items: center; gap: 8px; font-weight: 700; }
  .brand__dot { border-radius: 50%; background: var(--blue); flex: none; }
  .card--front .brand { position: absolute; left: 34px; top: 40px; color: var(--blue); font-size: 28px; }
  .card--front .brand__dot { width: 22px; height: 22px; }

  .person { position: absolute; left: 34px; top: 130px; }
  .person__name { color: var(--blue); font-size: 22px; font-weight: 700; margin-bottom: 14px; }

  .contacts { display: grid; grid-template-columns: 150px 1fr; row-gap: 8px; column-gap: 14px; font-size: 14px; color: var(--ink); }
  .contact { display: flex; align-items: center; gap: 8px; white-space: nowrap; }
  .contact--wide { grid-column: 1 / span 2; }
  .icon { width: 14px; height: 14px; fill: var(--blue); flex: none; }

  .card--back .brand-block { position: absolute; left: 50%; top: 50%; transform: translate(-50%, -50%); text-align: left; }
  .card--back .brand { color: var(--blue); font-size: 48px; }
  .card--back .brand__dot { width: 40px; height: 40px; }
  .brand-block__url { color: var(--lime); font-size: 13px; letter-spacing: 4px; margin: 4px 0 0 50px; }
</style>
</head>
<body>
  <section class="card card--front" aria-label="Business card front">
    <div class="ghost-mark" aria-hidden="true"></div>
    <div class="accent accent--lime"></div>
    <div class="brand"><span class="brand__dot"></span>Oru Loft</div>
    <div class="person">
      <h1 class="person__name">Dara Whitcombe</h1>
      <div class="contacts">
        <div class="contact">
          <svg class="icon" viewBox="0 0 16 16"><path d="M3 1h3l1 4-2 1c1 2 3 4 5 5l1-2 4 1v3c0 1-1 2-2 2C7 15 1 9 1 3c0-1 1-2 2-2z"/></svg>0455 318 260
        </div>
        <div class="contact">
          <svg class="icon" viewBox="0 0 16 16"><path d="M1 3h14v10H1z M2 4l6 5 6-5" fill="none" stroke="var(--blue)" stroke-width="1.6"/></svg>dara@oruloft.com.au
        </div>
        <div class="contact">
          <svg class="icon" viewBox="0 0 16 16"><path d="M4 1h8v14H4z M6 12h4" fill="none" stroke="var(--blue)" stroke-width="1.8"/></svg>0455 318 260
        </div>
        <div class="contact">
          <svg class="icon" viewBox="0 0 16 16"><circle cx="8" cy="8" r="6.5" fill="none" stroke="var(--blue)" stroke-width="1.5"/><path d="M1.5 8h13M8 1.5c-3 3-3 10 0 13M8 1.5c3 3 3 10 0 13" fill="none" stroke="var(--blue)" stroke-width="1.2"/></svg>www.oruloft.com.au
        </div>
        <div class="contact contact--wide">
          <svg class="icon" viewBox="0 0 16 16"><path d="M8 1a5 5 0 0 1 5 5c0 4-5 9-5 9S3 10 3 6a5 5 0 0 1 5-5z"/><circle cx="8" cy="6" r="2" fill="#fff"/></svg>12 Larkfield Lane, Suite 4, Milbrook, NC 27000
        </div>
      </div>
    </div>
  </section>

  <section class="card card--back" aria-label="Business card back">
    <div class="accent accent--lime"></div>
    <div class="accent accent--blue"></div>
    <div class="brand-block">
      <div class="brand"><span class="brand__dot"></span>Oru Loft</div>
      <p class="brand-block__url">www.oruloft.com.au</p>
    </div>
  </section>
</body>
</html>
```